design for locksmith business

I need new logo, letterhead, business card and envelope designed for new mobile locksmith business.
Start off with a Logo but keep in mind that i want it to be used on all obove things listed.
Once a good logo is designed i will be more than happy to increase payment to have all listed designed.
Business Name: Ambergate Locksmiths
Slogan (We come to you 24/7)
www.ambergatelocksmiths.com.au
tam@ambergatelocksmiths.com.au
Phone: TBA
Mobile Locksmith business
Services Offered:
Residential
Commercial
Automotive
Safes
24/7 Fast Reliable Service

I think the logo should be modern and maybe show that we are a mobile service so maybe add underneath in small letters (We come to you 24/7)

Also keep in mind the design will be uniform across all business card, letterheads, Envelopes and web pages.

Once i have found a good logo i am more than happy to increase payment to have the other things (Business cards etc... designed to go with the logo.

Target Market(s)

Residential and commercial clients needing lock repairs on site

Industry/Entity Type

Locksmith

```html
<!DOCTYPE html>
<html lang="en">
<head>
<meta charset="utf-8">
<title>Ambergate Locksmiths – Identity</title>
<link href="https://fonts.googleapis.com/css2?family=Questrial&family=Open+Sans:wght@400&display=swap" rel="stylesheet">
<style>
  :root {
    --ink: #000000;
    --paper: #ffffff;
    --skyline: #ececed;
    --skyline-deep: #e2e2e3;
    --shadow: #d9d9d9;
    --frame: #8a8a8a;
    --muted: #c9c9c9;
  }
  html, body { margin: 0; padding: 0; overflow: hidden; }
  body { width: 1200px; height: 998px; background: var(--paper); position: relative; font-family: "Questrial", sans-serif; }
  .abs { position: absolute; }

  .city-backdrop { left: 0; top: 645px; width: 1200px; height: 210px;
    background: linear-gradient(to bottom, rgba(236,236,237,0) 0%, var(--skyline) 35%, var(--skyline-deep) 100%); }
  .base-band { left: 0; top: 852px; width: 1200px; height: 146px; background: var(--ink); }

  .mark { border-radius: 50%; background: var(--ink); }
  .wordmark { color: var(--ink); text-align: center; line-height: 1; }

  .main-mark { left: 274px; top: 228px; width: 96px; height: 96px; }
  .main-wordmark { left: 110px; top: 432px; width: 430px; font-size: 72px; line-height: 82px; }

  .sheet { background: var(--paper); overflow: hidden; }
  .sheet-shadow { background: var(--shadow); }
  .sheet .sky { position: absolute; left: 0; width: 100%;
    background: linear-gradient(to bottom, rgba(236,236,237,0.2), var(--skyline) 40%, var(--skyline)); }
  .sheet .band { position: absolute; left: 0; bottom: 0; width: 100%; background: var(--ink);
    color: var(--paper); font-family: "Open Sans", sans-serif; text-align: right; box-sizing: border-box; }
  .sheet .slogan { position: absolute; right: 8px; color: var(--muted); font-family: "Open Sans", sans-serif; }
  .sheet .logo { position: absolute; text-align: center; }
  .sheet .logo .mark { margin: 0 auto; }

  .letterhead { left: 672px; top: 72px; width: 466px; height: 595px; border: 1px solid var(--frame); box-sizing: border-box; }
  .letterhead-shadow { left: 655px; top: 420px; width: 30px; height: 280px; transform: skewY(-8deg); }
  .letterhead .sky { top: 418px; height: 130px; }
  .letterhead .band { height: 47px; padding: 5px 12px 0 0; font-size: 9.5px; line-height: 13px; }
  .letterhead .slogan { top: 536px; font-size: 9px; }
  .letterhead .logo { left: 18px; top: 450px; width: 90px; }

  .envelope-shadow { left: 570px; top: 205px; width: 30px; height: 200px; transform: skewY(-10deg); }
  .envelope { left: 590px; top: 158px; width: 496px; height: 237px; border: 1px solid var(--frame); box-sizing: border-box; }
  .envelope .sky { top: 62px; height: 128px; }
  .envelope .band { height: 47px; padding: 5px 12px 0 0; font-size: 8.5px; line-height: 12.5px; }
  .envelope .slogan { top: 178px; font-size: 8.5px; }
  .envelope .logo { left: 14px; top: 88px; width: 88px; }

  .card-shadow { left: 158px; top: 770px; width: 262px; height: 170px; background: #7a7a7a; transform: rotate(-3deg); }
  .card { left: 152px; top: 758px; width: 266px; height: 168px; border: 1px solid var(--frame); box-sizing: border-box; transform: rotate(-3deg); }
  .card .sky { top: 20px; height: 110px; }
  .card .band { height: 40px; padding: 5px 8px 0 0; font-size: 6.2px; line-height: 9.5px; }
  .card .slogan { top: 112px; font-size: 7px; }
  .card .logo { left: 10px; top: 30px; width: 100px; }

  .reverse-mark { left: 1061px; top: 866px; width: 30px; height: 30px; background: var(--paper); }
  .reverse-wordmark { left: 990px; top: 934px; width: 172px; font-size: 24px; line-height: 27px; color: var(--paper); }
</style>
</head>
<body>
  <div class="abs city-backdrop" role="img" aria-label="Soft grey city skyline silhouette"></div>
  <div class="abs base-band"></div>

  <div class="abs mark main-mark"></div>
  <div class="abs wordmark main-wordmark">Ambergate<br>Locksmiths</div>

  <div class="abs sheet-shadow letterhead-shadow"></div>
  <div class="abs sheet letterhead">
    <div class="sky" role="img" aria-label="Pale grey city skyline silhouette"></div>
    <div class="logo">
      <div class="mark" style="width:22px;height:22px;"></div>
      <div class="wordmark" style="font-size:15px;line-height:17px;margin-top:16px;">Ambergate<br>Locksmiths</div>
    </div>
    <div class="slogan">We come to you 24/7</div>
    <div class="band">www.ambergatelocksmiths.com.au &nbsp;• tam@ambergatelocksmiths.com.au • Phone: TBA<br>Mobile Locksmith business<br>Services Offered: Residential, Commercial, Automotive, Safes</div>
  </div>

  <div class="abs sheet-shadow envelope-shadow"></div>
  <div class="abs sheet envelope">
    <div class="sky" role="img" aria-label="Pale grey city skyline silhouette"></div>
    <div class="logo">
      <div class="mark" style="width:22px;height:22px;"></div>
      <div class="wordmark" style="font-size:15px;line-height:17px;margin-top:16px;">Ambergate<br>Locksmiths</div>
    </div>
    <div class="slogan">We come to you 24/7</div>
    <div class="band">www.ambergatelocksmiths.com.au &nbsp;• tam@ambergatelocksmiths.com.au • Phone: TBA<br>Mobile Locksmith business<br>Services Offered: Residential, Commercial, Automotive, Safes</div>
  </div>

  <div class="abs card-shadow"></div>
  <div class="abs sheet card">
    <div class="sky" role="img" aria-label="Pale grey city skyline silhouette"></div>
    <div class="logo">
      <div class="mark" style="width:20px;height:20px;"></div>
      <div class="wordmark" style="font-size:16px;line-height:18px;margin-top:14px;">Ambergate<br>Locksmiths</div>
    </div>
    <div class="slogan">We come to you 24/7</div>
    <div class="band">www.ambergatelocksmiths.com.au • tam@ambergatelocksmiths.com.au • Phone: TBA<br>Mobile Locksmith business<br>Services Offered: Residential, Commercial, Automotive, Safes</div>
  </div>

  <div class="abs mark reverse-mark"></div>
  <div class="abs wordmark reverse-wordmark">Ambergate<br>Locksmiths</div>
</body>
</html>
```